Retail Seafood business needs package/label design

In need of packaging/label design for multiple seafood products such as sword fish, halibut, cod fish, scallops, mahi, catfish, and lobster tails

```html
<!DOCTYPE html>
<html lang="en">
<head>
<meta charset="utf-8">
<title>Seafood Packaging – Shrimp &amp; Pangasius</title>
<link rel="stylesheet" href="https://fonts.googleapis.com/css2?family=Lobster+Two:ital,wght@1,700&family=Montserrat:wght@700&family=Roboto+Condensed:wght@400&display=swap">
<style>
  :root {
    --page-bg: #ffffff;
    --band-blue: #1b8fd0;
    --band-stripe: #4fb0e4;
    --body-blue-top: #1a7cc4;
    --body-navy: #0f1f6b;
    --body-deep: #0b1650;
    --wave-white: #ffffff;
    --wave-black: #1f1f1f;
    --bottom-black: #222222;
    --bottom-stripe: #333333;
    --title-white: #ffffff;
    --title-edge: #1574c6;
    --tagline-blue: #2aa9e8;
    --info-white: #f2f2f2;
    --shrimp-light: #f7b48a;
    --shrimp-deep: #e0622f;
    --fillet-light: #fbeaea;
    --fillet-pink: #e58a97;
    --fillet-cream: #f1ece3;
  }
  html, body {
    margin: 0;
    width: 1200px;
    height: 847px;
    overflow: hidden;
    background: var(--page-bg);
  }
  .shelf {
    position: relative;
    width: 1200px;
    height: 847px;
  }
  .package {
    position: absolute;
    top: 143px;
    width: 376px;
    height: 545px;
  }
  .package--shrimp { left: 197px; }
  .package--pangasius { left: 632px; }

  .top-band { fill: var(--band-blue); }
  .band-stripe { stroke: var(--band-stripe); stroke-width: 1; }
  .wave-black { fill: var(--wave-black); }
  .wave-white { fill: var(--wave-white); }
  .bottom-panel { fill: var(--bottom-black); }
  .bottom-stripe { stroke: var(--bottom-stripe); stroke-width: 1; }

  .product-title {
    font-family: "Lobster Two", cursive;
    font-style: italic;
    font-weight: 700;
    font-size: 64px;
    fill: var(--title-white);
    stroke: var(--title-edge);
    stroke-width: 2.2px;
    paint-order: stroke fill;
  }
  .tagline {
    font-family: "Montserrat", sans-serif;
    font-weight: 700;
    font-size: 12.5px;
    letter-spacing: 1.6px;
    fill: var(--tagline-blue);
  }
  .storage-note, .net-weight {
    font-family: "Roboto Condensed", sans-serif;
    fill: var(--info-white);
  }
  .storage-note { font-size: 11px; }
  .net-weight--label { font-size: 7.5px; }
  .net-weight--value { font-size: 10.5px; }
</style>
</head>
<body>
<main class="shelf">

  <!-- Shrimp package -->
  <svg class="package package--shrimp" viewBox="0 0 376 545" aria-labelledby="shrimp-name">
    <defs>
      <linearGradient id="shrimp-body" x1="0" y1="0" x2="0" y2="1">
        <stop offset="0" stop-color="var(--body-blue-top)"/>
        <stop offset="0.55" stop-color="var(--body-navy)"/>
        <stop offset="1" stop-color="var(--body-deep)"/>
      </linearGradient>
      <linearGradient id="shrimp-window" x1="0" y1="0" x2="1" y2="1">
        <stop offset="0" stop-color="var(--shrimp-light)"/>
        <stop offset="0.5" stop-color="var(--shrimp-deep)"/>
        <stop offset="1" stop-color="var(--shrimp-light)"/>
      </linearGradient>
      <linearGradient id="shrimp-hero" x1="0" y1="0" x2="1" y2="1">
        <stop offset="0" stop-color="#f08a4e"/>
        <stop offset="1" stop-color="#f6d2bf"/>
      </linearGradient>
      <path id="shrimp-tagline-path" d="M18 281 C60 310 140 312 196 268"/>
    </defs>

    <rect class="product-window" x="0" y="240" width="376" height="200" fill="url(#shrimp-window)" role="img" aria-label="Photo of cooked farmed shrimp inside the bag"/>
    <path class="wave-black" d="M0 318 C60 356 150 350 230 310 C290 282 340 272 376 276 L376 0 L0 0 Z"/>
    <path class="wave-white" d="M0 306 C60 344 150 338 230 298 C290 270 340 260 376 264 L376 0 L0 0 Z"/>
    <path d="M0 296 C60 334 150 328 230 288 C290 260 340 250 376 254 L376 0 L0 0 Z" fill="url(#shrimp-body)"/>

    <rect class="top-band" x="0" y="0" width="376" height="42"/>
    <g class="band-stripes">
      <line class="band-stripe" x1="0" y1="8" x2="376" y2="8"/>
      <line class="band-stripe" x1="0" y1="14" x2="376" y2="14"/>
      <line class="band-stripe" x1="0" y1="20" x2="376" y2="20"/>
      <line class="band-stripe" x1="0" y1="26" x2="376" y2="26"/>
      <line class="band-stripe" x1="0" y1="32" x2="376" y2="32"/>
      <line class="band-stripe" x1="0" y1="38" x2="376" y2="38"/>
    </g>

    <rect class="hero-photo" x="128" y="28" width="244" height="166" rx="10" fill="url(#shrimp-hero)" role="img" aria-label="Photo of peeled cooked shrimp with tails"/>

    <text id="shrimp-name" class="product-title" x="26" y="245">Shrimp</text>
    <text class="tagline"><textPath href="#shrimp-tagline-path">CAMARON DE CULTIVO</textPath></text>

    <path class="bottom-panel" d="M0 412 C70 440 190 350 300 362 C340 366 362 382 376 396 L376 545 L0 545 Z"/>
    <g class="bottom-stripes">
      <line class="bottom-stripe" x1="0" y1="506" x2="376" y2="506"/>
      <line class="bottom-stripe" x1="0" y1="514" x2="376" y2="514"/>
      <line class="bottom-stripe" x1="0" y1="522" x2="376" y2="522"/>
      <line class="bottom-stripe" x1="0" y1="530" x2="376" y2="530"/>
    </g>
    <text class="storage-note" x="24" y="468">KEEP FROZEN</text>
    <text class="storage-note" x="24" y="480">MANTENGASE REFRIGERADO</text>
    <text class="net-weight net-weight--label" x="358" y="467" text-anchor="end">NET WT / CONTENIDO NETO</text>
    <text class="net-weight net-weight--value" x="358" y="480" text-anchor="end">4.8 OZ (3LB) 1.36 KG</text>
  </svg>

  <!-- Pangasius package -->
  <svg class="package package--pangasius" viewBox="0 0 376 545" aria-labelledby="pangasius-name">
    <defs>
      <linearGradient id="pangasius-body" x1="0" y1="0" x2="0" y2="1">
        <stop offset="0" stop-color="var(--body-blue-top)"/>
        <stop offset="0.55" stop-color="var(--body-navy)"/>
        <stop offset="1" stop-color="var(--body-deep)"/>
      </linearGradient>
      <linearGradient id="pangasius-window" x1="0" y1="0" x2="1" y2="1">
        <stop offset="0" stop-color="var(--fillet-light)"/>
        <stop offset="0.55" stop-color="var(--fillet-pink)"/>
        <stop offset="1" stop-color="var(--fillet-light)"/>
      </linearGradient>
      <linearGradient id="pangasius-hero" x1="0" y1="0" x2="1" y2="1">
        <stop offset="0" stop-color="#ffffff"/>
        <stop offset="1" stop-color="var(--fillet-cream)"/>
      </linearGradient>
      <path id="pangasius-tagline-path" d="M18 281 C60 310 140 312 196 268"/>
    </defs>

    <rect class="product-window" x="0" y="240" width="376" height="200" fill="url(#pangasius-window)" role="img" aria-label="Photo of raw farmed fish fillets inside the bag"/>
    <path class="wave-black" d="M0 318 C60 356 150 350 230 310 C290 282 340 272 376 276 L376 0 L0 0 Z"/>
    <path class="wave-white" d="M0 306 C60 344 150 338 230 298 C290 270 340 260 376 264 L376 0 L0 0 Z"/>
    <path d="M0 296 C60 334 150 328 230 288 C290 260 340 250 376 254 L376 0 L0 0 Z" fill="url(#pangasius-body)"/>

    <rect class="top-band" x="0" y="0" width="376" height="42"/>
    <g class="band-stripes">
      <line class="band-stripe" x1="0" y1="8" x2="376" y2="8"/>
      <line class="band-stripe" x1="0" y1="14" x2="376" y2="14"/>
      <line class="band-stripe" x1="0" y1="20" x2="376" y2="20"/>
      <line class="band-stripe" x1="0" y1="26" x2="376" y2="26"/>
      <line class="band-stripe" x1="0" y1="32" x2="376" y2="32"/>
      <line class="band-stripe" x1="0" y1="38" x2="376" y2="38"/>
    </g>

    <rect class="hero-photo" x="162" y="54" width="206" height="128" rx="10" fill="url(#pangasius-hero)" role="img" aria-label="Photo of a white fish fillet garnished with parsley"/>

    <text id="pangasius-name" class="product-title" x="26" y="236">Pangasius</text>
    <text class="tagline"><textPath href="#pangasius-tagline-path">FILETE DE CULTIVO</textPath></text>

    <path class="bottom-panel" d="M0 412 C70 440 190 350 300 362 C340 366 362 382 376 396 L376 545 L0 545 Z"/>
    <g class="bottom-stripes">
      <line class="bottom-stripe" x1="0" y1="506" x2="376" y2="506"/>
      <line class="bottom-stripe" x1="0" y1="514" x2="376" y2="514"/>
      <line class="bottom-stripe" x1="0" y1="522" x2="376" y2="522"/>
      <line class="bottom-stripe" x1="0" y1="530" x2="376" y2="530"/>
    </g>
    <text class="storage-note" x="24" y="468">KEEP FROZEN</text>
    <text class="storage-note" x="24" y="480">MANTENGASE REFRIGERADO</text>
    <text class="net-weight net-weight--label" x="364" y="467" text-anchor="end">NET WT / CONTENIDO NETO</text>
    <text class="net-weight net-weight--value" x="364" y="480" text-anchor="end">4.8 OZ (3LB) 1.36 KG</text>
  </svg>

</main>
</body>
</html>
```